Stationary set for consulting company
Tarvo Bridge
Creative Brief
Modern
Karim Yusuf Al Banna
Co-Founder
Reef Spire, Abu Dhabi United Arab Emirates
karim@tarvobridge.ae
www.tarvobridge.com
I need a full stationary set for the company logo I will be attaching. (PPTs, business cards, envelope, letterhead, etc)

```html
<!DOCTYPE html>
<html lang="en">
<head>
<meta charset="utf-8">
<title>Tarvo Bridge – Business Card</title>
<link href="https://fonts.googleapis.com/css2?family=Montserrat:wght@400;600;700&display=swap" rel="stylesheet">
<style>
  :root {
    --navy: #1d4a8a;
    --sky: #a9c8ea;
    --white: #ffffff;
    --backdrop: #d9d9d9;
  }
  * { margin: 0; padding: 0; box-sizing: border-box; }
  html, body { width: 1200px; height: 989px; overflow: hidden; }
  body {
    background: var(--backdrop);
    font-family: "Montserrat", sans-serif;
    position: relative;
  }
  .card {
    position: absolute;
    left: 235px;
    width: 730px;
    height: 385px;
    overflow: hidden;
  }
  .card-front { top: 75px; background: var(--white); }
  .card-back { top: 525px; background: var(--navy); }

  .brand {
    display: flex;
    align-items: center;
    gap: 12px;
    font-weight: 700;
    letter-spacing: 1px;
    text-transform: uppercase;
  }
  .brand-dot { border-radius: 50%; flex: none; }

  .card-front .brand {
    position: absolute;
    left: 48px;
    top: 62px;
    color: var(--navy);
    font-size: 24px;
  }
  .card-front .brand-dot { width: 34px; height: 34px; background: var(--navy); }

  .holder {
    position: absolute;
    right: 40px;
    top: 70px;
    text-align: right;
    text-transform: uppercase;
  }
  .holder-name { color: var(--navy); font-weight: 700; font-size: 13px; letter-spacing: .3px; }
  .holder-role { color: var(--sky); font-weight: 600; font-size: 12px; margin-top: 3px; }

  .band {
    position: absolute;
    left: 0;
    top: 220px;
    width: 730px;
    height: 165px;
  }
  .contact {
    position: absolute;
    left: 52px;
    top: 252px;
    color: var(--white);
    font-size: 12px;
    line-height: 17px;
    text-transform: uppercase;
  }
  .contact strong { font-weight: 700; }

  .card-back .brand {
    position: absolute;
    left: 0; right: 0;
    top: 160px;
    justify-content: center;
    color: var(--white);
    font-size: 36px;
    letter-spacing: 2px;
  }
  .card-back .brand-dot { width: 44px; height: 44px; background: var(--white); }
  .back-web {
    position: absolute;
    left: 0; right: 0;
    top: 292px;
    text-align: center;
    color: var(--white);
    font-size: 12px;
    text-transform: uppercase;
  }
  .back-web strong { font-weight: 700; }
</style>
</head>
<body>
  <section class="card card-front">
    <div class="brand"><span class="brand-dot"></span>Tarvo Bridge</div>
    <div class="holder">
      <div class="holder-name">Karim Yusuf Al Banna</div>
      <div class="holder-role">Co-Founder</div>
    </div>
    <svg class="band" viewBox="0 0 730 165" aria-hidden="true">
      <rect width="730" height="165" fill="var(--navy)"/>
      <polygon points="520,0 536,0 446,165 430,165" fill="var(--white)"/>
      <polygon points="560,0 574,0 484,165 470,165" fill="var(--white)"/>
      <polygon points="590,0 730,0 730,165 500,165" fill="var(--sky)"/>
    </svg>
    <div class="contact">
      Reef Spire, Abu Dhabi<br>
      United Arab Emirates<br>
      <strong>Phone:</strong> +971-50-4310958<br>
      <strong>Email:</strong> karim@tarvobridge.ae<br>
      <strong>Web:</strong> www.tarvobridge.com
    </div>
  </section>

  <section class="card card-back">
    <div class="brand"><span class="brand-dot"></span>Tarvo Bridge</div>
    <div class="back-web"><strong>Web:</strong> www.tarvobridge.com</div>
  </section>
</body>
</html>
```